RK Bastone Construction Inc.

Design a new business card for our construction company
To be removed from current card:
Delete 25 years
Delete Tenant fit up Renovations section

```html
<!DOCTYPE html>
<html lang="en">
<head>
<meta charset="utf-8">
<title>RK Bastone Construction Inc. – Business Card</title>
<link rel="stylesheet" href="https://fonts.googleapis.com/css2?family=Saira:wght@400;600&display=swap">
<style>
  :root {
    --backdrop: #999999;
    --card: #ffffff;
    --ink: #4f2d6b;
  }
  * { margin: 0; padding: 0; box-sizing: border-box; }
  html, body {
    width: 1200px; height: 1000px; overflow: hidden;
    background: var(--backdrop);
    font-family: "Saira", sans-serif;
    color: var(--ink);
  }
  .card {
    position: absolute;
    width: 615px; height: 351px;
    background: var(--card);
  }
  .card--front { left: 293px; top: 100px; }
  .card--back  { left: 295px; top: 511px; }

  .brand-name {
    font-weight: 600;
    color: var(--ink);
    white-space: nowrap;
    letter-spacing: 0.01em;
  }
  .card--front .brand-name {
    position: absolute; left: 0; right: 0; top: 156px;
    text-align: center; font-size: 27px;
  }
  .card--back .brand-name {
    position: absolute; right: 35px; top: 42px;
    font-size: 16px;
  }

  .website {
    position: absolute; left: 0; right: 0; top: 296px;
    display: flex; justify-content: center; align-items: center; gap: 5px;
    font-size: 18px;
  }
  .icon { width: 13px; height: 13px; fill: var(--ink); flex: none; }

  .holder-name {
    position: absolute; left: 46px; top: 186px;
    font-size: 23px; font-weight: 600;
  }
  .contact-list {
    position: absolute; left: 46px; top: 240px;
    list-style: none; font-size: 19px; line-height: 22px;
  }
  .contact-list li { display: flex; align-items: center; gap: 12px; }
  .contact-list .email { font-size: 17px; }
  .address {
    position: absolute; left: 399px; top: 238px;
    font-style: normal; font-size: 19px; line-height: 23px;
  }
</style>
</head>
<body>
  <section class="card card--front">
    <div class="brand-name">RK Bastone Construction Inc.</div>
    <div class="website">
      <svg class="icon" viewBox="0 0 16 16" aria-hidden="true">
        <path d="M8 1a7 7 0 1 0 0 14A7 7 0 0 0 8 1zm0 1.5c.8 0 1.7 1.3 2.1 3.5H5.9C6.3 3.8 7.2 2.5 8 2.5zM5.7 7h4.6a11 11 0 0 1 0 2H5.7a11 11 0 0 1 0-2zM2.6 7h2.1a12 12 0 0 0 0 2H2.6a5.5 5.5 0 0 1 0-2zm8.7 0h2.1a5.5 5.5 0 0 1 0 2h-2.1a12 12 0 0 0 0-2zM3.1 6a5.5 5.5 0 0 1 2.9-3A8 8 0 0 0 4.9 6zm8 0a8 8 0 0 0-1.1-3 5.5 5.5 0 0 1 2.9 3zM3.1 10h1.8A8 8 0 0 0 6 13a5.5 5.5 0 0 1-2.9-3zm2.8 0h4.2c-.4 2.2-1.3 3.5-2.1 3.5S6.3 12.2 5.9 10zm5.2 0h1.8A5.5 5.5 0 0 1 10 13a8 8 0 0 0 1.1-3z"/>
      </svg>
      <span>www.rkbastoneconst.ca</span>
    </div>
  </section>

  <section class="card card--back">
    <div class="brand-name">RK Bastone Construction Inc.</div>
    <h1 class="holder-name">Marco Bastone</h1>
    <ul class="contact-list">
      <li>
        <svg class="icon" viewBox="0 0 16 16" aria-hidden="true"><path d="M4 1h8a1 1 0 0 1 1 1v12a1 1 0 0 1-1 1H4a1 1 0 0 1-1-1V2a1 1 0 0 1 1-1zm1 2v8h6V3zm3 9a1 1 0 1 0 0 2 1 1 0 0 0 0-2z"/></svg>
        <span>613-555-0142</span>
      </li>
      <li>
        <svg class="icon" viewBox="0 0 16 16" aria-hidden="true"><path d="M1 5c0-2 3-3 7-3s7 1 7 3v1.5h-3.5V5h-7v1.5H1zm3 2.5h8l2 6H2zm4 1.5a2 2 0 1 0 0 4 2 2 0 0 0 0-4z"/></svg>
        <span>613-555-0187</span>
      </li>
      <li class="email">
        <svg class="icon" viewBox="0 0 16 16" aria-hidden="true"><path d="M1 3.5h14v1L8 9 1 4.5zm0 2.4 7 4.5 7-4.5V12.5H1z"/></svg>
        <span>marco@rkbastoneconst.ca</span>
      </li>
    </ul>
    <address class="address">
      2180 Ridgeway Rd<br>
      Suite 210, Ottawa<br>
      ON K1B 4T7
    </address>
  </section>
</body>
</html>
```